Pregnancy and Fertility Information Website

Hello Designers,
I need a website which provide tips and information about healthy and happy pregnancy. My website name is Lorvin medical.

The website should provide all the information needed throughout pregnancy and beyond ranging from pregnancy tracking tools and articles about common pregnancy concerns and what to expect during pregnancy,etc.
The details about first trimester, second trimester and third trimester should be highlighted in the website.

Top Navigation
Home, Fertility, Pregnancy basics, Articles, Tips and News

I'm looking for a simple and clean design which involves captivating images and colors but it shouldn't be crowded. The design must be professional and modern. An easy to navigate layout is a must.

Green, violet, blue and light yellow colors are my favorites but i'm open to other options.

Any questions. Kindly ask

Industry/Entity Type

Medical

```html
<!DOCTYPE html>
<html lang="en">
<head>
<meta charset="utf-8">
<title>Lorvin medical – Pregnancy &amp; Fertility</title>
<link href="https://fonts.googleapis.com/css2?family=Roboto:wght@300;400;500;700;900&display=swap" rel="stylesheet">
<style>
:root{
  --violet:#7b6fa6;
  --violet-dark:#6a5f96;
  --green:#4fae44;
  --green-soft:#e4f2e1;
  --blue-soft:#e6eef7;
  --ink:#222;
  --muted:#666;
  --line:#dcdcdc;
  --page:#ffffff;
  --panel:#f0f0f0;
}
*{box-sizing:border-box;margin:0;padding:0}
html,body{width:1200px;height:3689px;overflow:hidden}
body{position:relative;font-family:'Roboto',sans-serif;color:var(--ink);background:var(--page)}
.abs{position:absolute}
.photo{position:absolute}

/* header + hero */
.hero{position:absolute;left:0;top:0;width:1200px;height:615px;background:linear-gradient(90deg,#f6f5f3 0%,#efedea 45%,#e9e4df 100%);overflow:hidden}
.hero-photo{right:0;top:0;width:760px;height:615px;background:linear-gradient(120deg,#ece7e2 0%,#d9c7bb 40%,#5f7fd0 62%,#e8e3de 85%)}
.brand{left:88px;top:40px;display:flex;align-items:center;gap:10px;font-weight:700;font-size:17px;color:var(--violet);white-space:nowrap}
.brand .dot{width:22px;height:22px;border-radius:50%;background:var(--green)}
.nav a{position:absolute;font-size:11px;font-weight:700;color:#333;text-decoration:none;letter-spacing:.3px;white-space:nowrap}
.urgent{left:656px;top:34px;width:196px;height:45px;border-radius:23px;background:var(--violet);color:#fff;font-size:11px;font-weight:700;display:flex;align-items:center;justify-content:center;gap:10px}
.hero h1{left:88px;top:182px;font-weight:500;font-size:32px;line-height:1;text-transform:uppercase}
.hero h1 span{display:block;font-size:48px;font-weight:700;margin-top:10px}
.hero p{left:88px;top:296px;width:330px;font-size:11px;line-height:20px;color:#555}
.btn{position:absolute;height:38px;border-radius:19px;display:flex;align-items:center;gap:12px;padding-left:14px;font-size:10px;font-weight:700;text-transform:uppercase}
.btn-green{left:88px;top:444px;width:212px;background:var(--green);color:#fff}
.btn-white{left:88px;top:502px;width:212px;background:#fff;border:1px solid var(--line);color:#333}
.dots{left:102px;top:575px;display:flex;gap:8px;align-items:center}
.dots i{width:10px;height:10px;border-radius:50%;background:var(--violet);display:block}
.dots i.on{width:20px;height:20px;background:#fff;border:2px solid var(--violet)}

/* featured */
.section-title{position:absolute;left:0;width:1200px;text-align:center;font-size:22px;font-weight:500}
.title-rule{position:absolute;left:430px;width:340px;height:1px;background:var(--line)}
.tab{position:absolute;top:0;width:130px;height:80px;text-align:center;font-size:10px;font-weight:500;text-transform:uppercase;color:#333}
.tab svg{display:block;margin:8px auto 10px}
.tab.active{background:var(--violet);color:#fff;border:2px solid var(--violet-dark)}
.sort{left:829px;top:844px;display:flex;align-items:center;gap:12px;font-size:9px;font-weight:700}
.sort .select{width:142px;height:36px;border-radius:18px;background:#eee;display:flex;align-items:center;justify-content:space-between;padding:0 16px;font-size:9px}
.arrow{position:absolute;top:850px;width:30px;height:30px;border-radius:50%;border:1px solid #bbb;display:flex;align-items:center;justify-content:center}
.card{position:absolute;overflow:hidden}
.card .shade{position:absolute;left:0;right:0;bottom:0;height:55%;background:linear-gradient(transparent,rgba(0,0,0,.78))}
.tag{position:absolute;background:var(--green);color:#fff;font-size:8px;font-weight:700;padding:4px 8px;text-transform:uppercase}
.meta{position:absolute;display:flex;align-items:center;gap:8px;font-size:8px;font-weight:500;text-transform:uppercase;white-space:nowrap}
.meta .av{width:28px;height:28px;border-radius:50%;background:#c9a48c;border:2px solid #fff}
.card h3{position:absolute;left:24px;right:20px;font-size:17px;font-weight:700;color:#fff}
.card .ex{position:absolute;left:24px;right:20px;font-size:11px;line-height:14px;color:#fff}
.small h3{position:static;color:var(--ink);font-size:18px;line-height:22px;margin-top:20px}
.small .ex{position:static;color:#333;margin-top:14px;font-size:11px;line-height:13px}
.read-all{left:494px;top:1832px;width:212px;height:38px;border-radius:19px;border:1px solid #ccc;display:flex;align-items:center;justify-content:center;font-size:9px;font-weight:700}

/* trimester */
.trimester{position:absolute;left:0;top:1943px;width:1200px;height:996px;background:var(--violet)}
.trimester .section-title{color:#fff;top:72px}
.tri-tab{position:absolute;top:174px;width:186px;height:116px;text-align:center;color:#fff;font-size:11px;font-weight:500;text-transform:uppercase}
.tri-tab small{display:block;font-size:8px;opacity:.8;margin-top:4px}
.tri-tab.active{background:var(--green)}
.tri-tab .pict{width:22px;height:40px;border-radius:11px;background:var(--green);margin:20px auto 10px}
.tri-tab.active .pict{background:#fff}
.tri-card{position:absolute;left:88px;top:322px;width:1033px;height:612px;background:#fff;box-shadow:0 4px 14px rgba(0,0,0,.2)}
.tri-card h2{position:absolute;left:34px;top:36px;font-size:22px;font-weight:500}
.stats{position:absolute;left:34px;top:94px;font-size:10px;line-height:22px;white-space:nowrap}
.stats b{display:inline-block;width:160px;font-weight:700}
.tri-card .body{position:absolute;left:34px;top:206px;width:660px;font-size:11px;line-height:20px;color:#444}
.box{position:absolute;top:290px;width:290px;height:280px;padding:22px 26px}
.box h4{font-size:12px;font-weight:700;margin-bottom:20px}
.box li{list-style:none;font-size:10px;display:flex;align-items:center;gap:12px;margin-bottom:20px}
.box li i{width:14px;height:14px;border-radius:50%;background:var(--green);display:block}
.grind{left:34px;background:var(--blue-soft)}
.bump{left:334px;background:var(--green-soft)}
.body-art{left:720px;top:110px;width:250px;height:470px;border-radius:120px;background:linear-gradient(180deg,#f2f2f2,#e4e4e4 50%,#efefef)}

/* calculator */
.calc{position:absolute;left:0;top:2939px;width:1200px;height:516px;background:var(--panel)}
.calc .q{position:absolute;left:148px;top:48px;font-size:11px;font-weight:500}
.calc h2{position:absolute;left:148px;top:66px;font-size:24px;font-weight:500}
.field{position:absolute;height:42px;border-radius:21px;background:#fff;border:1px solid #ddd;display:flex;align-items:center;justify-content:space-between;padding:0 18px;font-size:9px;font-weight:700}
.calc .lbl{position:absolute;left:98px;top:244px;font-size:10px;font-weight:700}
.submit{left:88px;top:373px;width:132px;height:40px;border-radius:20px;background:var(--green);color:#fff;font-size:10px;font-weight:700;display:flex;align-items:center;justify-content:center}
.calc .note{position:absolute;left:98px;top:428px;font-size:10px;color:#555}

/* footer */
.footer{position:absolute;left:0;top:3455px;width:1200px;height:234px;background:#fff}
.foot-brand{left:520px;top:-20px;width:160px;height:116px;background:#fff;border-radius:50%;display:flex;align-items:center;justify-content:center;gap:8px;font-weight:700;color:var(--violet);font-size:15px;white-space:nowrap}
.foot-brand .dot{width:14px;height:14px;border-radius:50%;background:var(--green)}
.social{top:52px;width:34px;height:34px;border-radius:50%;background:#d6d6d6}
.email{left:770px;top:48px;width:312px;height:42px;border-radius:21px;background:#f2f2f2;display:flex;align-items:center;padding-left:60px;font-size:9px;color:#999}
.go{left:1044px;top:46px;width:46px;height:46px;border-radius:50%;background:var(--green);color:#fff;font-size:10px;font-weight:700;display:flex;align-items:center;justify-content:center}
.foot-nav{top:142px;left:0;width:1200px;border-top:1px solid #eee;height:37px}
.foot-nav a{position:absolute;top:14px;font-size:10px;font-weight:700;color:#333;text-decoration:none}
.copy{top:179px;left:0;width:1200px;height:55px;background:#f3f3f3;text-align:center;line-height:55px;font-size:8px;color:#888}
</style>
</head>
<body>

<header class="hero">
  <div class="photo hero-photo" role="img" aria-label="Smiling pregnant woman in a blue top relaxing on a white sofa"></div>
  <div class="abs brand"><span class="dot"></span>Lorvin medical</div>
  <nav class="abs nav" style="left:0;top:48px">
    <a href="#" style="left:278px">FERTILITY</a>
    <a href="#" style="left:354px">PREGNANCY BASICS</a>
    <a href="#" style="left:477px">ARTICLES</a>
    <a href="#" style="left:575px">TIPS &amp; NEWS</a>
  </nav>
  <div class="abs urgent">
    <svg width="20" height="18" viewBox="0 0 20 18" fill="none" stroke="#fff" stroke-width="1.5"><circle cx="7" cy="6" r="4"/><path d="M1 17c0-4 3-6 6-6s6 2 6 6"/><rect x="12" y="1" width="7" height="5" rx="1"/></svg>
    I NEED URGENT ADVICE
  </div>
  <h1 class="abs">Things to avoid during<span>Pregnancy</span></h1>
  <p class="abs">There are a number of things a pregnant woman should be cautious of, or avoid during pregnancy, including cleaning products, massages, saunas, foods, X-rays, hair dye, seafoods and fake tans.</p>
  <div class="btn btn-green"><svg width="16" height="14" viewBox="0 0 16 14" fill="none" stroke="#fff" stroke-width="1.5"><rect x="1" y="1" width="14" height="12" rx="1"/><path d="M4 5h8M4 9h5"/></svg>Read full article</div>
  <div class="btn btn-white"><svg width="16" height="16" viewBox="0 0 16 16" fill="none" stroke="#555" stroke-width="1.5"><rect x="1" y="2" width="14" height="13"/><path d="M1 6h14M5 0v4M11 0v4"/></svg>Calculate your due date</div>
  <div class="abs dots"><i class="on"></i><i></i><i></i><i></i></div>
</header>

<h2 class="section-title" style="top:672px">Featured articles</h2>
<div class="title-rule" style="top:733px"></div>
<svg class="abs" style="left:577px;top:715px;background:#fff;padding:0 6px" width="48" height="36" viewBox="0 0 48 36" fill="none" stroke="#333" stroke-width="2"><rect x="6" y="4" width="36" height="28" rx="2"/><path d="M12 12h12M12 18h24M12 24h24M28 10h8v4h-8z"/></svg>

<div class="abs tabs" style="left:0;top:828px">
  <div class="tab" style="left:63px"><svg width="34" height="34" viewBox="0 0 34 34" fill="none" stroke="#555" stroke-width="1.5"><circle cx="17" cy="17" r="15"/><circle cx="17" cy="17" r="5"/></svg>Pregnancy</div>
  <div class="tab" style="left:184px"><svg width="34" height="34" viewBox="0 0 34 34" fill="none" stroke="#555" stroke-width="1.5"><rect x="3" y="6" width="28" height="22"/><path d="M8 24c4-10 14-10 18 0"/></svg>Your first scan</div>
  <div class="tab active" style="left:320px;width:135px"><svg width="34" height="34" viewBox="0 0 34 34" fill="none" stroke="#fff" stroke-width="1.5"><path d="M24 4l6 6L12 28H6v-6z"/><path d="M20 8l6 6"/></svg>Pregnancy test</div>
  <div class="tab" style="left:440px"><svg width="34" height="34" viewBox="0 0 34 34" fill="none" stroke="#555" stroke-width="1.5"><circle cx="17" cy="17" r="15"/><path d="M14 26c-3-6 1-14 7-14"/></svg>Trimester</div>
  <div class="tab" style="left:545px"><svg width="34" height="34" viewBox="0 0 34 34" fill="none" stroke="#555" stroke-width="1.5"><circle cx="7" cy="17" r="3"/><circle cx="17" cy="17" r="3"/><circle cx="27" cy="17" r="3"/></svg>More</div>
</div>
<div class="abs sort">SORT BY: <div class="select">POSTED TODAY <svg width="10" height="6" viewBox="0 0 10 6" fill="none" stroke="#333" stroke-width="1.5"><path d="M1 1l4 4 4-4"/></svg></div></div>
<div class="arrow" style="left:1054px;border-color:#333"><svg width="8" height="12" viewBox="0 0 8 12" fill="none" stroke="#333" stroke-width="1.5"><path d="M7 1L2 6l5 5"/></svg></div>
<div class="arrow" style="left:1094px"><svg width="8" height="12" viewBox="0 0 8 12" fill="none" stroke="#999" stroke-width="1.5"><path d="M1 1l5 5-5 5"/></svg></div>

<article class="card" style="left:88px;top:944px;width:246px;height:411px">
  <div class="photo" style="inset:0;background:linear-gradient(180deg,#2a1d16,#6b4a36 55%,#241812)" role="img" aria-label="Pregnant woman dancing with one arm raised"></div>
  <div class="shade"></div>
  <span class="tag" style="left:24px;top:256px">Nutrition</span>
  <div class="meta" style="left:24px;top:282px;color:#fff"><span class="av"></span>Mara Ellison &nbsp;|&nbsp; 25 Jan, 2017</div>
  <h3 style="top:322px">Multiple pregnancy</h3>
  <p class="ex" style="top:350px">Multiple pregnancy means carrying more than one baby, normally twins.</p>
</article>
<article class="card" style="left:352px;top:944px;width:506px;height:411px">
  <div class="photo" style="inset:0;background:linear-gradient(135deg,#4d4a28,#8a8752 45%,#b8b8a0 70%,#5c5a34)" role="img" aria-label="Pregnant woman in a light sweater standing in a forest"></div>
  <div class="shade"></div>
  <span class="tag" style="left:24px;top:244px">Health</span>
  <div class="meta" style="left:24px;top:270px;color:#fff"><span class="av"></span>Mara Ellison &nbsp;|&nbsp; 25 Jan, 2017</div>
  <h3 style="top:310px">Is it safe to get a flu shot when I'm pregnant?</h3>
  <p class="ex" style="top:346px">The Northfield Health Council, the Alder College of Obstetric Care and Gynecologists, the Brightwell Midwives Guild.</p>
</article>
<article class="card" style="left:875px;top:944px;width:246px;height:411px">
  <div class="photo" style="inset:0;background:linear-gradient(180deg,#e9e6e2,#d7c8bd 50%,#6b5a4e)" role="img" aria-label="Pregnant woman holding a bowl of salad"></div>
  <div class="shade"></div>
  <span class="tag" style="left:24px;top:244px">Nutrition</span>
  <div class="meta" style="left:24px;top:270px;color:#fff"><span class="av"></span>Mara Ellison &nbsp;|&nbsp; 25 Jan, 2017</div>
  <h3 style="top:310px">Can running a fever ..</h3>
  <p class="ex" style="top:342px">Yes, running a fever can be dangerous during pregnancy.</p>
</article>

<article class="card small" style="left:88px;top:1375px;width:246px;height:400px">
  <div class="photo" style="left:0;top:0;width:246px;height:214px;background:linear-gradient(135deg,#cbb9a6,#c9454e 55%,#8a7868)" role="img" aria-label="Pregnant woman in a red dress sitting on a couch with a glass of water"></div>
  <span class="tag" style="left:14px;top:186px">Nutrition</span>
  <div style="position:absolute;top:234px;left:0;width:240px">
    <div class="meta" style="position:static;color:#555"><span class="av"></span>Mara Ellison &nbsp;|&nbsp; 25 Jan, 2017</div>
    <h3>Is it safe to take antibiotics during pregnancy?</h3>
    <p class="ex">Multiple pregnancy means carrying more than one baby, normally twins.</p>
  </div>
</article>
<article class="card small" style="left:352px;top:1375px;width:246px;height:400px">
  <div class="photo" style="left:0;top:0;width:246px;height:214px;background:linear-gradient(135deg,#f2f0ee,#d9b5b8 55%,#e6e3e0)" role="img" aria-label="Pregnant woman drinking a glass of water"></div>
  <span class="tag" style="left:14px;top:186px">Nutrition</span>
  <div style="position:absolute;top:234px;left:0;width:240px">
    <div class="meta" style="position:static;color:#555"><span class="av"></span>Mara Ellison &nbsp;|&nbsp; 25 Jan, 2017</div>
    <h3>Urinary tract infections during pregnancy</h3>
    <p class="ex">Multiple pregnancy means carrying more than one baby, normally twins.</p>
  </div>
</article>
<article class="card small" style="left:613px;top:1375px;width:246px;height:400px">
  <div class="photo" style="left:0;top:0;width:246px;height:214px;background:linear-gradient(135deg,#6c8b4c,#a9b99a 50%,#4f6a3a)" role="img" aria-label="Pregnant woman jogging outdoors"></div>
  <span class="tag" style="left:14px;top:186px">Nutrition</span>
  <div style="position:absolute;top:234px;left:0;width:240px">
    <div class="meta" style="position:static;color:#555"><span class="av"></span>Mara Ellison &nbsp;|&nbsp; 25 Jan, 2017</div>
    <h3>Yeast infections during pregnancy</h3>
    <p class="ex">Multiple pregnancy means carrying more than one baby, normally twins.</p>
  </div>
</article>
<article class="card small" style="left:875px;top:1375px;width:246px;height:400px">
  <div class="photo" style="left:0;top:0;width:246px;height:214px;background:linear-gradient(135deg,#ede9e4,#d8cfc6 55%,#b8aba0)" role="img" aria-label="Pregnant woman resting in bed"></div>
  <span class="tag" style="left:14px;top:186px">Nutrition</span>
  <div style="position:absolute;top:234px;left:0;width:240px">
    <div class="meta" style="position:static;color:#555"><span class="av"></span>Mara Ellison &nbsp;|&nbsp; 25 Jan, 2017</div>
    <h3>Pregnancy medicine cabinet checklist</h3>
    <p class="ex">Multiple pregnancy means carrying more than one baby, normally twins.</p>
  </div>
</article>

<div class="abs read-all">READ ALL ARTICLES</div>

<section class="trimester">
  <h2 class="section-title">Trimester Chart</h2>
  <div class="title-rule" style="top:123px;background:rgba(255,255,255,.35)"></div>
  <svg class="abs" style="left:573px;top:104px;background:var(--violet);padding:0 12px" width="54" height="38" viewBox="0 0 30 38" fill="none" stroke="#fff" stroke-width="1.5"><circle cx="15" cy="19" r="13"/><path d="M12 28c-3-6 1-14 7-14"/></svg>
  <div class="tri-tab" style="left:303px"><div class="pict" role="img" aria-label="Early pregnancy figure icon"></div>First Trimester<small>0 to 13 weeks</small></div>
  <div class="tri-tab" style="left:480px"><div class="pict" role="img" aria-label="Mid pregnancy figure icon"></div>Second Trimester<small>14 to 27 weeks</small></div>
  <div class="tri-tab active" style="left:688px"><div class="pict" role="img" aria-label="Late pregnancy figure icon"></div>Third Trimester<small>28 to 42 weeks</small></div>

  <div class="tri-card">
    <h2>Third Trimester(28th Week)</h2>
    <div class="abs sort" style="left:740px;top:24px">SORT BY WEEK: <div class="select" style="width:140px">28TH WEEK <svg width="10" height="6" viewBox="0 0 10 6" fill="none" stroke="#333" stroke-width="1.5"><path d="M1 1l4 4 4-4"/></svg></div></div>
    <div class="stats">
      <div><b>Gestational age:</b>27 weeks and 0 - 6 days</div>
      <div><b>Embryonic age:</b>25 weeks and 0 - 6 days</div>
      <div><b>Average crown to heel length:</b>37.6 cm (14.80 inches)</div>
      <div><b>Average weight:</b>1005 grams (2.22 pounds)</div>
    </div>
    <p class="body">The brain develops rapidly. The nervous system develops enough to control some body functions. The eyelids open and close. The cochleae are now developed, though the myelin sheaths in neural portion of the auditory system will continue to develop until 18 months after birth. The respiratory system, while immature, has developed to the point where gas exchange.</p>
    <div class="box grind"><h4>THE GRIND</h4><ul>
      <li><i></i>Sleeping problems</li><li><i></i>Shortness of breath</li><li><i></i>Aches and Pains</li><li><i></i>Braxton Hicks contractions</li><li><i></i>Leaky breasts</li></ul></div>
    <div class="box bump"><h4>THE BUMP</h4><ul>
      <li><i></i>Baby's about 14 inches/3 pounds</li><li><i></i>Fatter/with reduced wrinkles</li><li><i></i>Lungs are fully-matured</li></ul></div>
    <div class="abs body-art" role="img" aria-label="Grey pregnant body outline with a green circle showing the baby at 28 weeks"></div>
  </div>
</section>

<section class="calc">
  <svg class="abs" style="left:88px;top:50px" width="40" height="40" viewBox="0 0 40 40" fill="none" stroke="#333" stroke-width="2"><rect x="2" y="6" width="36" height="32"/><path d="M2 14h36M11 2v8M29 2v8M9 20h4M18 20h4M27 20h4M9 28h4M18 28h4M27 28h4"/></svg>
  <div class="q">What was the date of the first day of your last period?</div>
  <h2>Calculate your due date</h2>
  <div class="field" style="left:88px;top:160px;width:136px">DAY <svg width="10" height="6" viewBox="0 0 10 6" fill="none" stroke="#333" stroke-width="1.5"><path d="M1 1l4 4 4-4"/></svg></div>
  <div class="field" style="left:238px;top:160px;width:142px">MONTH <svg width="10" height="6" viewBox="0 0 10 6" fill="none" stroke="#333" stroke-width="1.5"><path d="M1 1l4 4 4-4"/></svg></div>
  <div class="field" style="left:394px;top:160px;width:140px">YEAR <svg width="10" height="6" viewBox="0 0 10 6" fill="none" stroke="#333" stroke-width="1.5"><path d="M1 1l4 4 4-4"/></svg></div>
  <div class="lbl">Adjusted cycle length</div>
  <div class="field" style="left:88px;top:268px;width:94px">28 <svg width="10" height="6" viewBox="0 0 10 6" fill="none" stroke="#333" stroke-width="1.5"><path d="M1 1l4 4 4-4"/></svg></div>
  <div class="abs submit">SUBMIT</div>
  <p class="note">If your cycle is shorter or longer than 28 days, please adjust the number above.</p>
  <div class="photo" style="left:787px;top:24px;width:413px;height:492px;background:linear-gradient(180deg,#f0f0f0,#e6cfc6 30%,#d64d8a 60%,#eeeeee)" role="img" aria-label="Pregnant woman in a pink top holding her belly"></div>
</section>

<footer class="footer">
  <div class="abs foot-brand"><span class="dot"></span>Lorvin medical</div>
  <span class="abs social" style="left:272px"></span>
  <span class="abs social" style="left:316px"></span>
  <span class="abs social" style="left:360px"></span>
  <span class="abs social" style="left:404px"></span>
  <div class="abs email"><svg class="abs" style="left:24px;top:14px" width="22" height="14" viewBox="0 0 22 14" fill="none" stroke="#aaa" stroke-width="1.5"><rect x="1" y="1" width="20" height="12"/><path d="M1 1l10 7 10-7"/></svg>ENTER EMAIL ADDRESS</div>
  <div class="abs go">GO</div>
  <nav class="abs foot-nav">
    <a href="#" style="left:330px">FERTILITY</a>
    <a href="#" style="left:486px">PREGNANCY BASICS</a>
    <a href="#" style="left:654px">ARTICLES</a>
    <a href="#" style="left:774px">TIPS &amp; NEWS</a>
  </nav>
  <div class="abs copy">© 2017 LORVIN MEDICAL. ALL RIGHTS RESERVED</div>
</footer>

</body>
</html>
```